BrPeople Business Cards for SME Experts

We need a business card for a new company based in Clearwater FL called Brightfold of People. BrP is your access to on-demand subject matter experts. The final design should be very clean communicating innovation and expertise. Our logo design is attached.

The Information Age has affected the workforce in that automation and computerization have resulted in higher productivity coupled with net job loss of many knowledgeable employees. Combined with the creation of the internet and search capabilities, the disintermediation of the value chain of Subject Matter Experts (SME) has happened. We no longer need to work through traditional consulting firms for all consulting needs, instead the direct access to the SME, through a leaner and lower cost model is what the market is demanding.
BrPeople is a new marketplace to buy consulting services. The business model is that all consultants (subject matter experts) can become a consulting resource in the marketplace following our guidelines. The consumer can now easily access consultants that they could not find easily before.
In much the way an Zaxo car can be identified and requested, so can a BrPeople Consultant. Each consultant can be identified by: location, expertise, billing rate, and prior experience rating.
By seamlessly connecting consultants to requesters through a new Brightfold of People marketplace, you now will have an easy to use and quicker turnaround to request and staff your consulting needs. Leveraging the BrP app, you can access the subject matter expert you need for your business requirement.

Target Market(s)

Small and medium sized companies; non-profits

Industry/Entity Type

Business Consultant

Contact Information for Business Card

Name
website
email address
Logo
mailing address (debating if I really need...)
twitter
LinkedIn

Requirements
Must have
• the logo I have included in the design; want the colors to be consistent with the logo design

```html
<!DOCTYPE html>
<html lang="en">
<head>
<meta charset="utf-8">
<title>Brightfold of People – Business Card</title>
<link href="https://fonts.googleapis.com/css2?family=Arimo:wght@400;700&display=swap" rel="stylesheet">
<style>
  :root {
    --page-bg: #e9ebef;
    --navy-dark: #141f5c;
    --navy: #1d2c73;
    --teal: #1ba6cc;
    --teal-light: #37c3e0;
    --white: #ffffff;
    --back-light: #fafafa;
    --back-shade: #d9d9db;
    --ink: #1d2c73;
    --muted: #3a3f55;
  }
  * { box-sizing: border-box; margin: 0; padding: 0; }
  html, body {
    width: 1200px; height: 950px; overflow: hidden;
    background: var(--page-bg);
    font-family: "Arimo", Arial, sans-serif;
  }
  .sheet {
    width: 1200px; height: 950px;
    display: flex; flex-direction: column; align-items: center;
    justify-content: center; gap: 50px;
  }
  .card {
    position: relative; width: 700px; height: 400px; overflow: hidden;
    box-shadow: 0 10px 30px rgba(20, 31, 92, 0.18);
  }

  /* Back side */
  .card--back {
    background: linear-gradient(135deg, var(--back-light) 0%, var(--white) 40%, var(--back-shade) 100%);
    display: flex; flex-direction: column; align-items: center; justify-content: center;
  }
  .brand-mark {
    display: flex; align-items: center; justify-content: center;
    width: 110px; height: 110px; border-radius: 50%;
    border: 6px solid var(--teal);
    color: var(--ink); font-weight: 700; font-size: 38px;
  }
  .card--back .wordmark {
    margin-top: 26px; color: var(--ink);
    font-size: 34px; font-weight: 700; letter-spacing: 2px;
  }
  .card--back .site {
    margin-top: 10px; color: var(--muted);
    font-size: 18px; letter-spacing: 2px;
  }
  .card--back .rule {
    margin-top: 18px; width: 360px; height: 1px; background: var(--muted); opacity: .5;
  }

  /* Front side */
  .card--front {
    background: linear-gradient(120deg, var(--navy-dark) 0%, var(--navy) 70%);
    color: var(--white);
  }
  .front-accent { position: absolute; inset: 0; }
  .social-row { position: absolute; left: 34px; top: 30px; display: flex; gap: 10px; }
  .social-dot { width: 24px; height: 24px; border-radius: 50%; background: var(--teal); }
  .contact { position: absolute; left: 34px; top: 150px; }
  .contact .name { color: var(--teal-light); font-size: 22px; font-weight: 700; letter-spacing: 1px; }
  .contact .role { margin-top: 6px; font-size: 17px; letter-spacing: 1px; }
  .contact .lines { margin-top: 22px; list-style: none; }
  .contact .lines li {
    display: flex; align-items: center; gap: 10px;
    font-size: 16px; letter-spacing: .5px; margin-bottom: 6px;
  }
  .contact .lines svg { flex: none; }
  .card--front .wordmark {
    position: absolute; left: 34px; top: 318px;
    font-size: 26px; font-weight: 700; letter-spacing: 2px; color: var(--white);
  }
  .hero-mark {
    position: absolute; left: 420px; top: 55px;
    width: 290px; height: 290px; border-radius: 50%;
    border: 14px solid var(--white);
    display: flex; align-items: center; justify-content: center;
    font-size: 96px; font-weight: 700; color: var(--white);
  }
</style>
</head>
<body>
<main class="sheet">
  <section class="card card--back" aria-label="Card back">
    <div class="brand-mark">BrP</div>
    <p class="wordmark">Brightfold of People</p>
    <p class="site">BrightfoldofPeople.com</p>
    <div class="rule"></div>
  </section>

  <section class="card card--front" aria-label="Card front">
    <svg class="front-accent" width="700" height="400" viewBox="0 0 700 400" aria-hidden="true">
      <defs>
        <linearGradient id="accentFade" x1="0" y1="0" x2="1" y2="1">
          <stop offset="0" stop-color="#1ba6cc"/>
          <stop offset="1" stop-color="#37c3e0"/>
        </linearGradient>
      </defs>
      <polygon points="560,0 700,0 700,400 470,400" fill="url(#accentFade)"/>
      <polygon points="470,0 560,0 470,400 380,400" fill="#2a3a86" opacity=".55"/>
    </svg>

    <div class="social-row">
      <span class="social-dot"></span>
      <span class="social-dot"></span>
    </div>

    <div class="contact">
      <p class="name">Daniel Reyes</p>
      <p class="role">Consultant</p>
      <ul class="lines">
        <li>
          <svg width="16" height="12" viewBox="0 0 16 12"><rect x="0.5" y="0.5" width="15" height="11" fill="#37c3e0"/><path d="M1 1 L8 7 L15 1" stroke="#141f5c" stroke-width="1.4" fill="none"/></svg>
          Daniel@BrightfoldofPeople.com
        </li>
        <li>
          <svg width="16" height="16" viewBox="0 0 16 16"><circle cx="8" cy="8" r="7" fill="#37c3e0"/><path d="M1 8 H15 M8 1 C4 5 4 11 8 15 M8 1 C12 5 12 11 8 15" stroke="#141f5c" stroke-width="1" fill="none"/></svg>
          BrightfoldofPeople.com
        </li>
      </ul>
    </div>

    <p class="wordmark">Brightfold of People</p>

    <div class="hero-mark">BrP</div>
  </section>
</main>
</body>
</html>
```